Healthy Supplement featuring Moringa products

Need 3 business card options for our reps to order from Printwell. Our reps will be ordering from Printwell once we upload them. Attached is our current designs to show what info needs to be on the cards. Our website is www.tqvitality.com
The business cards will be a template for our reps to order from. Most of our reps are Asian & Hispanic. Please look at our website so you can see who we are to get the look and feel what we need.
Target Market(s)
Adults 30 on up. Health oriented people.
Industry/Entity Type
Health And Wellness
Contact Information for Business Card
Name
Title
Phone
Logo
www.tqvitality.com/my/username
Font styles to use
Requirements
Must have
- Please match our website look and colors. A moringa leaf is nice, but am open to something different.
Nice to have
- Healthy looking and warm, not super cold or too modern.
Should not have
- No harsh colors please.

```html
<!DOCTYPE html>
<html lang="en">
<head>
<meta charset="utf-8">
<title>TQ Vitality Business Card</title>
<link href="https://fonts.googleapis.com/css2?family=Libre+Baskerville:ital@0;1&family=Roboto:wght@300;400;700&display=swap" rel="stylesheet">
<style>
  :root {
    --backdrop: #2b2b2b;
    --paper: #ffffff;
    --leaf-green: #68a80e;
    --brand-green: #5f9f12;
    --accent-orange: #f3911f;
    --text-light: #ffffff;
    --divider: rgba(255,255,255,0.75);
  }
  * { margin: 0; padding: 0; box-sizing: border-box; }
  html, body {
    width: 1200px; height: 1108px; overflow: hidden;
    background: var(--backdrop);
  }
  .canvas {
    width: 1200px; height: 1108px;
    display: flex; flex-direction: column; align-items: center; justify-content: center;
    gap: 44px;
  }
  .card {
    width: 840px; height: 480px;
    border-bottom: 5px solid var(--accent-orange);
    position: relative;
  }
  .card--front {
    background: var(--paper);
    display: flex; align-items: center; justify-content: center;
  }
  .brand {
    display: flex; align-items: center; gap: 18px;
  }
  .brand__dot {
    width: 46px; height: 46px; border-radius: 50%;
    background: var(--brand-green);
  }
  .brand__name {
    font-family: "Libre Baskerville", serif;
    font-size: 54px; letter-spacing: 4px;
    color: var(--brand-green);
    text-transform: uppercase;
  }
  .card--back {
    background: var(--leaf-green);
    display: flex; align-items: center; justify-content: center;
    gap: 26px;
  }
  .identity { text-align: right; }
  .identity__name {
    font-family: "Libre Baskerville", serif;
    font-size: 27px; color: var(--accent-orange);
    line-height: 1.1;
  }
  .identity__title {
    font-family: "Roboto", sans-serif;
    font-weight: 700; font-size: 19px; color: var(--text-light);
    margin-top: 2px;
  }
  .divider {
    width: 1px; height: 96px; background: var(--divider);
  }
  .contact { list-style: none; }
  .contact__item {
    display: flex; align-items: center; gap: 14px;
    font-family: "Roboto", sans-serif; font-weight: 400;
    font-size: 21px; color: var(--text-light);
    line-height: 30px;
  }
  .contact__icon { width: 17px; height: 17px; fill: var(--accent-orange); flex: none; }
</style>
</head>
<body>
<main class="canvas">
  <section class="card card--front">
    <div class="brand">
      <span class="brand__dot"></span>
      <span class="brand__name">TQ Vitality</span>
    </div>
  </section>

  <section class="card card--back">
    <div class="identity">
      <p class="identity__name">Daniel Reyes</p>
      <p class="identity__title">President</p>
    </div>
    <span class="divider"></span>
    <ul class="contact">
      <li class="contact__item">
        <svg class="contact__icon" viewBox="0 0 24 24"><path d="M6.6 10.8c1.4 2.8 3.8 5.1 6.6 6.6l2.2-2.2c.3-.3.7-.4 1-.2 1.1.4 2.3.6 3.6.6.6 0 1 .4 1 1V20c0 .6-.4 1-1 1C10.6 21 3 13.4 3 4c0-.6.4-1 1-1h3.5c.6 0 1 .4 1 1 0 1.3.2 2.5.6 3.6.1.3 0 .7-.2 1l-2.3 2.2z"/></svg>
        <span>+1(555)214-3087</span>
      </li>
      <li class="contact__item">
        <svg class="contact__icon" viewBox="0 0 24 24"><path d="M2 5h20v14H2z M3 6l9 7 9-7" fill="var(--accent-orange)"/><path d="M3.5 6.5l8.5 6.5 8.5-6.5" stroke="var(--leaf-green)" stroke-width="1.6" fill="none"/></svg>
        <span>info@tqvitality.com</span>
      </li>
      <li class="contact__item">
        <svg class="contact__icon" viewBox="0 0 24 24"><circle cx="12" cy="12" r="10"/><path d="M2 12h20M12 2c3 3 3 17 0 20M12 2c-3 3-3 17 0 20" stroke="var(--leaf-green)" stroke-width="1.4" fill="none"/></svg>
        <span>www.tqvitality.com</span>
      </li>
    </ul>
  </section>
</main>
</body>
</html>
```